Entrepreneur Podcast Cover Graphic Design

My wife and I just launched our podcast but we don't like the current cover. We want a new cover designed so it stands out and reflects the professionalism of our podcast. Attached is our current podcast cover design. We'd like to have it read "Rob & Kalinda Interview Entrepreneurs on HARD TURNS" - We'd also like to feature somehow that we have daily tips included.

Target Market(s)

entrepreneurs,business owners,start ups

Industry/Entity Type

Entrepreneur

Font styles to use
Sans Serif

Colors
0355a3
f37122
9bcb3c
fbed22
ec1f27

Requirements
Must have
• Our names listed: Rob & Kalinda
Nice to have
• dark, bold colored background with an outline around the edge
Should not have
• no cartoons, no profanity

```html
<!DOCTYPE html>
<html lang="en">
<head>
<meta charset="utf-8">
<title>Rob &amp; Kalinda Interview Entrepreneurs on Hard Turns</title>
<link rel="stylesheet" href="https://fonts.googleapis.com/css2?family=Playfair+Display:ital,wght@0,400;0,700;0,900;1,900&display=swap">
<style>
  :root {
    --red: #c20018;
    --blue: #00008a;
    --white: #f2f2f2;
    --grey: #505050;
    --green: #80ff00;
    --green-edge: #6a6a6a;
    --badge: #1b1b1b;
  }
  html, body {
    margin: 0;
    width: 1200px;
    height: 1200px;
    overflow: hidden;
    background: var(--red);
  }
  .cover {
    display: block;
    width: 1200px;
    height: 1200px;
  }
  .cover__field { fill: var(--blue); }
  .cover__stitch {
    fill: none;
    stroke: var(--white);
    stroke-width: 1.5;
    stroke-dasharray: 6 5;
  }
  .hosts {
    font-family: "Playfair Display", serif;
    font-weight: 400;
    font-size: 190px;
    fill: var(--white);
  }
  .hosts__rule { stroke: var(--red); stroke-width: 3; }
  .tagline {
    font-family: "Playfair Display", serif;
    font-weight: 700;
    font-size: 64px;
    fill: var(--grey);
  }
  .topic {
    font-family: "Playfair Display", serif;
    fill: var(--green);
    stroke: var(--green-edge);
    stroke-width: 1.5;
    paint-order: stroke;
  }
  .topic__main { font-weight: 900; font-size: 250px; }
  .topic__sub { font-weight: 900; font-style: italic; font-size: 220px; }
  .topic__quote { font-weight: 900; font-size: 300px; }
  .badge__disc { fill: var(--badge); }
  .badge__label {
    font-family: "Playfair Display", serif;
    font-weight: 700;
    font-size: 56px;
    fill: var(--white);
  }
</style>
</head>
<body>
<svg class="cover" viewBox="0 0 1200 1200" xmlns="http://www.w3.org/2000/svg">
  <defs>
    <filter id="lift" x="-10%" y="-10%" width="120%" height="130%">
      <feDropShadow dx="6" dy="8" stdDeviation="6" flood-color="#000" flood-opacity="0.6"/>
    </filter>
  </defs>

  <polygon class="cover__field" points="0,156 400,0 760,0 1200,156 1200,1048 800,1200 376,1200 0,1048"/>
  <polygon class="cover__stitch" points="16,166 402,14 758,14 1184,166 1184,1038 798,1186 378,1186 16,1038"/>

  <text class="hosts" x="24" y="324" textLength="1162" lengthAdjust="spacingAndGlyphs">rob &amp; kalinda</text>
  <line class="hosts__rule" x1="224" y1="358" x2="1000" y2="358"/>

  <text class="tagline" x="592" y="452" text-anchor="middle" textLength="800" lengthAdjust="spacingAndGlyphs">interview entrepreneurs</text>
  <text class="tagline" x="592" y="518" text-anchor="middle">on</text>

  <g class="topic" filter="url(#lift)">
    <text class="topic__quote" x="2" y="752">&#8220;</text>
    <text class="topic__main" x="596" y="788" text-anchor="middle" textLength="968" lengthAdjust="spacingAndGlyphs">HARD</text>
    <text class="topic__sub" x="604" y="900" text-anchor="middle" textLength="990" lengthAdjust="spacingAndGlyphs">turns</text>
    <text class="topic__quote" x="1058" y="1090">&#8221;</text>
  </g>

  <g class="badge">
    <circle class="badge__disc" cx="1080" cy="1090" r="130"/>
    <text class="badge__label" x="1070" y="1062" text-anchor="middle">daily</text>
    <text class="badge__label" x="1070" y="1122" text-anchor="middle">tips</text>
  </g>
</svg>
</body>
</html>
```